Bref créative
Business Card for ecommerce technology company
Circuitry Supply Partners, LLC.
Professional
Paul Dunmore
President
457 Ridgeback Ave.
Fernvale, QX 58204
mark@quorvix.com
www.quorvix.com
Please send Business card so I will be able to edit it for other employees

```html
<!DOCTYPE html>
<html lang="en">
<head>
<meta charset="utf-8">
<title>Quorvix Stationery Set</title>
<link href="https://fonts.googleapis.com/css2?family=Exo+2:wght@400;600;700&display=swap" rel="stylesheet">
<style>
  :root {
    --backdrop: #eef0f1;
    --paper: #ffffff;
    --brand-blue: #1a6fd6;
    --brand-deep: #0b47a8;
    --brand-light: #3f9bf2;
    --ink: #3a4556;
    --ink-soft: #7d8794;
    --band-edge: #16243a;
    --shadow: rgba(20, 30, 50, 0.18);
  }
  * { box-sizing: border-box; margin: 0; padding: 0; }
  html, body { width: 1200px; height: 936px; overflow: hidden; }
  body {
    background: var(--backdrop);
    font-family: "Exo 2", Arial, sans-serif;
    color: var(--ink);
    position: relative;
  }
  .sheet {
    position: absolute;
    background: var(--paper);
    box-shadow: 0 3px 10px var(--shadow);
  }

  /* Brand lockup */
  .lockup { display: flex; align-items: center; gap: 8px; }
  .lockup-dot {
    border-radius: 50%;
    background: var(--brand-blue);
    flex: none;
  }
  .lockup-text { display: flex; flex-direction: column; }
  .lockup-name {
    font-weight: 700;
    color: var(--brand-blue);
    letter-spacing: 0.04em;
    line-height: 1;
  }
  .lockup-tag {
    font-weight: 400;
    color: var(--ink-soft);
    line-height: 1.2;
    margin-top: 2px;
  }

  /* Letterhead */
  .letterhead { left: 185px; top: 68px; width: 263px; height: 542px; }
  .letterhead .lockup { position: absolute; left: 16px; top: 26px; gap: 6px; }
  .letterhead .lockup-dot { width: 30px; height: 30px; }
  .letterhead .lockup-name { font-size: 17px; }
  .letterhead .lockup-tag { font-size: 6px; }
  .letterhead-contact {
    position: absolute; right: 14px; top: 20px;
    list-style: none; font-size: 6px; color: var(--ink-soft);
  }
  .letterhead-contact li { display: flex; align-items: center; gap: 4px; line-height: 12px; }
  .letterhead-contact svg { width: 6px; height: 6px; flex: none; }
  .letterhead-mark {
    position: absolute; left: 92px; top: 196px;
    width: 80px; height: 80px; border-radius: 50%;
    background: radial-gradient(circle, #e6effb 0%, #d4e3f7 100%);
  }

  /* Folder */
  .folder {
    left: 633px; top: 68px; width: 379px; height: 542px;
    background: radial-gradient(ellipse at 50% 50%, var(--brand-light) 0%, var(--brand-blue) 45%, var(--brand-deep) 100%);
  }
  .folder-band {
    position: absolute; left: 0; right: 0; top: 212px; height: 90px;
    background: var(--paper);
    border-top: 3px solid var(--band-edge);
    border-bottom: 3px solid var(--band-edge);
    display: flex; align-items: center; justify-content: center;
  }
  .folder-band .lockup { flex-direction: column; gap: 4px; text-align: center; }
  .folder-band .lockup-text { align-items: center; }
  .folder-band .lockup-dot { width: 32px; height: 32px; }
  .folder-band .lockup-name { font-size: 18px; }
  .folder-band .lockup-tag { font-size: 6px; }

  /* Business card front */
  .card-front { left: 43px; top: 645px; width: 202px; height: 96px; overflow: hidden; }
  .card-front .lockup { position: absolute; left: 8px; top: 10px; gap: 4px; }
  .card-front .lockup-dot { width: 18px; height: 18px; }
  .card-front .lockup-name { font-size: 12px; }
  .card-front .lockup-tag { font-size: 4px; }
  .card-person { position: absolute; left: 10px; top: 52px; font-size: 6px; line-height: 9px; }
  .card-person strong { font-weight: 600; color: var(--brand-deep); display: block; }
  .card-panel {
    position: absolute; right: 0; top: 0; width: 92px; height: 100%;
    background: linear-gradient(180deg, var(--brand-light), var(--brand-deep));
    color: #fff; font-size: 4.5px; line-height: 8px;
    padding: 22px 8px 0 10px; list-style: none;
  }

  /* Business card back */
  .card-back {
    left: 43px; top: 772px; width: 202px; height: 101px;
    display: flex; flex-direction: column; align-items: center; justify-content: center; gap: 8px;
  }
  .card-back .lockup-dot { width: 36px; height: 36px; }
  .card-back-web { font-size: 5px; color: var(--ink-soft); letter-spacing: 0.08em; }

  /* Envelope front */
  .envelope-front { left: 263px; top: 739px; width: 430px; height: 139px; }
  .envelope-front .lockup { position: absolute; left: 12px; top: 20px; gap: 5px; }
  .envelope-front .lockup-dot { width: 26px; height: 26px; }
  .envelope-front .lockup-name { font-size: 16px; }
  .envelope-front .lockup-tag { font-size: 5px; }
  .envelope-address { position: absolute; left: 14px; top: 58px; font-size: 6px; color: var(--ink-soft); }

  /* Envelope back */
  .envelope-back { left: 739px; top: 739px; width: 425px; height: 139px; overflow: hidden; }
  .envelope-flap {
    position: absolute; left: 0; right: 0; top: 0; height: 50px;
    background: linear-gradient(180deg, var(--brand-light), var(--brand-blue));
    display: flex; align-items: center; justify-content: center;
    color: #fff; font-size: 8px; letter-spacing: 0.35em;
  }
</style>
</head>
<body>

  <section class="sheet letterhead" aria-label="Letterhead">
    <div class="lockup">
      <span class="lockup-dot"></span>
      <div class="lockup-text">
        <span class="lockup-name">QUORVIX</span>
        <span class="lockup-tag">Circuitry Supply Partners, LLC.</span>
      </div>
    </div>
    <ul class="letterhead-contact">
      <li><svg viewBox="0 0 10 10"><circle cx="5" cy="4" r="3" fill="#1a6fd6"/></svg>457 Ridgeback Ave.</li>
      <li><svg viewBox="0 0 10 10"></svg>Fernvale, QX 58204</li>
      <li><svg viewBox="0 0 10 10"><rect x="1" y="1" width="8" height="8" rx="2" fill="#1a6fd6"/></svg>555-318-2046</li>
      <li><svg viewBox="0 0 10 10"><rect x="1" y="1" width="8" height="8" rx="2" fill="#1a6fd6"/></svg>555-318-2047</li>
      <li><svg viewBox="0 0 10 10"><rect x="1" y="1" width="8" height="8" rx="2" fill="#1a6fd6"/></svg>555-318-2048</li>
      <li><svg viewBox="0 0 10 10"><rect x="1" y="1" width="8" height="8" rx="2" fill="#1a6fd6"/></svg>mark@quorvix.com</li>
      <li><svg viewBox="0 0 10 10"><rect x="1" y="1" width="8" height="8" rx="2" fill="#1a6fd6"/></svg>www.quorvix.com</li>
    </ul>
    <div class="letterhead-mark" role="img" aria-label="Faint brand circle watermark"></div>
  </section>

  <section class="sheet folder" aria-label="Presentation folder">
    <div class="folder-band">
      <div class="lockup">
        <span class="lockup-dot"></span>
        <div class="lockup-text">
          <span class="lockup-name">QUORVIX</span>
          <span class="lockup-tag">Circuitry Supply Partners, LLC.</span>
        </div>
      </div>
    </div>
  </section>

  <section class="sheet card-front" aria-label="Business card front">
    <div class="lockup">
      <span class="lockup-dot"></span>
      <div class="lockup-text">
        <span class="lockup-name">QUORVIX</span>
        <span class="lockup-tag">Circuitry Supply Partners, LLC.</span>
      </div>
    </div>
    <p class="card-person"><strong>Paul Dunmore</strong>President</p>
    <ul class="card-panel">
      <li>457 Ridgeback Ave.</li>
      <li>Fernvale, QX 58204</li>
      <li>555-318-2046</li>
      <li>mark@quorvix.com</li>
      <li>www.quorvix.com</li>
    </ul>
  </section>

  <section class="sheet card-back" aria-label="Business card back">
    <span class="lockup-dot"></span>
    <span class="card-back-web">www.quorvix.com</span>
  </section>

  <section class="sheet envelope-front" aria-label="Envelope front">
    <div class="lockup">
      <span class="lockup-dot"></span>
      <div class="lockup-text">
        <span class="lockup-name">QUORVIX</span>
        <span class="lockup-tag">Circuitry Supply Partners, LLC.</span>
      </div>
    </div>
    <p class="envelope-address">457 Ridgeback Ave. Fernvale, QX 58204</p>
  </section>

  <section class="sheet envelope-back" aria-label="Envelope back">
    <div class="envelope-flap">www.quorvix.com</div>
  </section>

</body>
</html>
```